Stationary & Business Cards
Brimford Holdings
Project: Stationary & Business Cards
Stationary & Business Cards - Construction
Creative Brief
Simple
Dale Purcott
General Manager
P.O. Box 382 Ashbury CT 06218
Dale@BrimfordHoldings.com
ON THE STATIONARY ONLY: add our website www.BrimfordHoldings.com
logo to fill in entire back of business card. (Red background with blue lettering)

```html
<!DOCTYPE html>
<html lang="en">
<head>
<meta charset="utf-8">
<title>Brimford Holdings — Stationery &amp; Business Cards</title>
<link href="https://fonts.googleapis.com/css2?family=Open+Sans:wght@400;600;800&display=swap" rel="stylesheet">
<style>
  :root {
    --backdrop: #4d4d4d;
    --paper: #ffffff;
    --navy: #243f7a;
    --red: #d22f3c;
    --ink: #555555;
    --faint: #e9e9e9;
  }
  * { margin: 0; padding: 0; box-sizing: border-box; }
  html, body { width: 1200px; height: 739px; overflow: hidden; background: var(--backdrop); }
  body { position: relative; font-family: "Open Sans", Arial, sans-serif; color: var(--ink); }

  .sheet { position: absolute; background: var(--paper); overflow: hidden; }

  .brand-name {
    font-family: "Open Sans", Arial, sans-serif;
    font-weight: 800;
    color: var(--navy);
    white-space: nowrap;
    letter-spacing: 0.02em;
    display: flex; align-items: center; gap: 5px;
    line-height: 1;
  }
  .brand-name .dot { width: 6px; height: 6px; background: var(--red); border-radius: 50%; flex: none; }
  .brand-name.faded { color: var(--faint); }
  .brand-name.stacked { flex-direction: column; align-items: flex-start; gap: 1px; }

  /* Business card front */
  .card-front { left: 34px; top: 247px; width: 182px; height: 103px; }
  .card-front .brand-name { position: absolute; left: 12px; top: 42px; font-size: 8px; }
  .card-front .divider { position: absolute; left: 84px; top: 22px; width: 1px; height: 60px; background: var(--red); }
  .card-front .holder { position: absolute; left: 92px; top: 22px; font-size: 5.5px; line-height: 1.5; }
  .card-front .holder .name { font-weight: 600; color: var(--navy); font-size: 6.5px; }
  .card-front .holder .title { margin-bottom: 7px; }

  /* Business card back */
  .card-back { left: 34px; top: 370px; width: 182px; height: 103px; background: var(--red);
    display: flex; align-items: center; justify-content: center; }
  .card-back .brand-name { font-size: 11px; }

  /* Letterhead */
  .letterhead { left: 250px; top: 67px; width: 432px; height: 610px; }
  .letterhead .brand-name { position: absolute; left: 26px; top: 24px; font-size: 15px; }
  .letterhead .contact { position: absolute; left: 318px; top: 18px; list-style: none; font-size: 6px; line-height: 1.65; }
  .letterhead .contact li { display: flex; align-items: center; gap: 4px; }
  .letterhead .contact .bullet { width: 4px; height: 4px; background: var(--red); border-radius: 50%; }
  .letterhead .contact .plain { padding-left: 8px; }
  .letterhead .watermark { position: absolute; left: 0; right: 0; top: 276px; justify-content: center; font-size: 27px; }

  /* Envelopes */
  .envelope-front { left: 715px; top: 67px; width: 447px; height: 183px; }
  .envelope-front .brand-name { position: absolute; left: 24px; top: 26px; font-size: 13px; }
  .envelope-front .return-address { position: absolute; left: 34px; top: 46px; font-size: 5.5px; }
  .envelope-front .watermark { position: absolute; right: 14px; top: 132px; font-size: 15px; }

  .envelope-back { left: 715px; width: 447px; height: 187px; }
  .envelope-back.red-flap { top: 281px; }
  .envelope-back.blue-flap { top: 499px; }
  .envelope-back svg { position: absolute; left: 0; top: 0; }
</style>
</head>
<body>

  <section class="sheet card-front" aria-label="Business card front">
    <div class="brand-name stacked"><span>BRIMFORD</span><span>HOLDINGS</span></div>
    <div class="divider"></div>
    <div class="holder">
      <div class="name">Dale Purcott</div>
      <div class="title">General Manager</div>
      <div>860.555.0142</div>
      <div>P.O. Box 382 Ashbury CT 06218</div>
      <div>Dale@BrimfordHoldings.com</div>
    </div>
  </section>

  <section class="sheet card-back" aria-label="Business card back">
    <div class="brand-name">BRIMFORD HOLDINGS</div>
  </section>

  <section class="sheet letterhead" aria-label="Letterhead">
    <div class="brand-name">BRIMFORD HOLDINGS <span class="dot"></span></div>
    <ul class="contact">
      <li class="plain">P.O. Box 382</li>
      <li class="plain">Ashbury CT 06218</li>
      <li><span class="bullet"></span>860.555.0142</li>
      <li><span class="bullet"></span>860.555.0143</li>
      <li><span class="bullet"></span>Dale@BrimfordHoldings.com</li>
      <li><span class="bullet"></span>www.BrimfordHoldings.com</li>
    </ul>
    <div class="brand-name faded watermark">BRIMFORD HOLDINGS</div>
  </section>

  <section class="sheet envelope-front" aria-label="Envelope front">
    <div class="brand-name">BRIMFORD HOLDINGS <span class="dot"></span></div>
    <div class="return-address">P.O. Box 382 Ashbury CT 06218</div>
    <div class="brand-name faded watermark">BRIMFORD HOLDINGS</div>
  </section>

  <section class="sheet envelope-back red-flap" aria-label="Envelope back with red flap">
    <svg width="447" height="187" viewBox="0 0 447 187">
      <path d="M0 0 H447 V10 Q447 22 420 30 L240 70 Q223 74 206 70 L27 30 Q0 22 0 10 Z" fill="var(--red)"/>
    </svg>
  </section>

  <section class="sheet envelope-back blue-flap" aria-label="Envelope back with blue flap">
    <svg width="447" height="187" viewBox="0 0 447 187">
      <path d="M0 0 H447 V10 Q447 22 420 30 L240 70 Q223 74 206 70 L27 30 Q0 22 0 10 Z" fill="var(--navy)"/>
    </svg>
  </section>

</body>
</html>
```